Holistic Health Coach needs a catchy and creative flyer

I need an eye-catching and convincing DL sized flyer for my new health coaching business. I provide advice and regular coaching to people on health, fitness and lifestyle issues.

I want these flyers to create awareness of my business as well as providing some information about what I do and the services that I can provide. I also want the flyers to have a strong and clear call-to-action so they can contact me.

I have provided some photos myself to be used in the flyer if necessary. I have also provided my logo. My Business name is called "Our Vital Ledger" however I want to market myself as a " Qualified Holistic Health Coach".

Target Market(s)

Men and Women of all ages who are trying to improve their health and fitness

Industry/Entity Type

Health And Wellness

Font styles to use
Sans Serif

Requirements
Must have
• My Business is called "Our Vital Ledger" (as seen in attached logo) but I would like the main marketing message of the flyer to be focused as " Qualified Holistic Health Coach" .
• The Flyer should be DL size.
• Strong call to action
• Catchy and memorable design- as I am a new business I want this to capture people's attention.
• Please see attached document for page content.
Nice to have
• I have also included some recent pictures of myself to be incorporated in the flyer, if appropriate.

```html
<!DOCTYPE html>
<html lang="en">
<head>
<meta charset="utf-8">
<title>Our Vital Ledger – DL Flyer</title>
<link href="https://fonts.googleapis.com/css2?family=Oswald:wght@500;600&family=Montserrat:wght@400;600;700&display=swap" rel="stylesheet">
<style>
:root{
  --stage:#e9e6e1;
  --green:#7cc242;
  --green-light:#a6d94f;
  --green-deep:#4f8f1f;
  --lime:#c6f03a;
  --band:#1d2416;
  --band-2:#2b3322;
  --white:#ffffff;
  --sky:#d9dccf;
  --grass:#6f8a3a;
}
*{margin:0;padding:0;box-sizing:border-box}
html,body{width:1200px;height:729px;overflow:hidden;background:var(--stage)}
body{position:relative;font-family:'Montserrat',sans-serif;color:var(--white)}
.flyer{position:absolute;width:668px;height:318px;overflow:hidden;box-shadow:0 6px 18px rgba(0,0,0,.25)}
.flyer--back{left:40px;top:76px;background:radial-gradient(ellipse at 45% 35%,var(--green-light),var(--green) 55%,var(--green-deep))}
.flyer--front{left:490px;top:340px}

.photo{position:absolute}
.back-photo{left:22px;top:90px;width:140px;height:172px;background:linear-gradient(180deg,#a9cf6a,#5f9a2a);border-radius:6px}

.name{font-family:'Oswald',sans-serif;font-weight:600;text-transform:uppercase;line-height:1;white-space:nowrap}
.back-heading{position:absolute;left:165px;top:38px;display:flex;align-items:flex-start;gap:6px}
.back-heading .name{font-size:22px}
.credentials{font-size:8px;font-weight:600;font-style:italic;color:var(--band);line-height:1.45;text-transform:uppercase;white-space:nowrap;padding-top:1px}

.brand{position:absolute;display:flex;align-items:center;gap:6px;font-weight:700;font-size:12px;letter-spacing:.5px;text-transform:uppercase;color:var(--white);white-space:nowrap}
.brand-dot{width:22px;height:22px;border-radius:50%;background:var(--white)}
.back-brand{right:24px;top:20px}

.section-title{position:absolute;left:165px;top:98px;font-size:14px;font-weight:400;letter-spacing:.5px;text-transform:uppercase;padding-bottom:3px;border-bottom:1px solid var(--white)}
.section-title b{font-weight:700}
.service-list{position:absolute;list-style:none;font-size:8.5px;font-weight:600;text-transform:uppercase;line-height:15.5px;white-space:nowrap}
.service-list li::before{content:"•";margin-right:5px}
.service-list--a{left:167px;top:127px}
.service-list--b{left:392px;top:119px}

.contact-band{position:absolute;left:0;bottom:0;width:100%;display:flex;align-items:center}
.back-band{height:56px;background:linear-gradient(90deg,var(--band),var(--band-2));padding-left:20px;gap:6px}
.mini-icon{width:28px;height:28px;border-radius:50%;background:var(--green);border:2px solid var(--lime);display:flex;align-items:center;justify-content:center}
.mini-icon svg{width:16px;height:16px}
.cta{font-family:'Oswald',sans-serif;font-weight:600;text-transform:uppercase;line-height:1;white-space:nowrap}
.back-band .cta{font-size:27px;color:var(--green);margin-left:14px}
.phones,.web{font-size:10.5px;font-weight:600;line-height:1.4;white-space:nowrap}
.back-band .phones{margin-left:16px}

.scene{position:absolute;inset:0;background:linear-gradient(180deg,var(--sky) 0%,#b8b99a 25%,var(--grass) 65%,#3e5a1c 100%)}
.front-photo{left:130px;top:14px;width:136px;height:262px;background:linear-gradient(180deg,#cfcfc9,#f2f2ee 40%,#3a3a3a 95%);border-radius:68px 68px 4px 4px}
.front-strip{position:absolute;left:0;top:108px;width:100%;height:97px;background:rgba(20,26,14,.82)}
.front-brand{left:16px;top:138px;font-size:12px}
.front-heading{position:absolute;left:308px;top:66px;display:flex;align-items:flex-end;gap:4px}
.front-heading .name{font-size:34px;letter-spacing:-.3px}
.tagline{font-family:'Oswald',sans-serif;font-weight:600;font-size:14px;line-height:1.1;color:var(--green-deep);text-transform:uppercase;white-space:nowrap;padding-bottom:2px}
.feature-row{position:absolute;left:306px;top:114px;display:flex;gap:4px}
.feature{width:78px;text-align:center;font-size:8.5px;text-transform:uppercase;line-height:1.3;white-space:nowrap}
.feature b{display:block;color:var(--lime);font-weight:700}
.feature-icon{width:50px;height:50px;margin:0 auto 6px;border-radius:50%;background:var(--green);border:3px solid var(--lime);display:flex;align-items:center;justify-content:center}
.feature-icon svg{width:28px;height:28px}
.front-band{height:48px;background:linear-gradient(90deg,rgba(124,194,66,.2),var(--green) 35%,var(--green));padding-left:208px;gap:12px}
.front-band .cta{font-size:24px;color:var(--white)}
</style>
</head>
<body>

<svg width="0" height="0" style="position:absolute" aria-hidden="true">
  <defs>
    <symbol id="icon-bowl" viewBox="0 0 24 24"><path d="M3 11h18a9 8 0 0 1-18 0z" fill="#fff"/><circle cx="8" cy="9" r="2.2" fill="#fff"/><circle cx="12.5" cy="8" r="2.6" fill="#fff"/><circle cx="17" cy="9.3" r="2" fill="#fff"/></symbol>
    <symbol id="icon-dumbbell" viewBox="0 0 24 24"><rect x="2" y="8" width="3" height="8" rx="1" fill="#fff"/><rect x="5" y="6" width="3" height="12" rx="1" fill="#fff"/><rect x="16" y="6" width="3" height="12" rx="1" fill="#fff"/><rect x="19" y="8" width="3" height="8" rx="1" fill="#fff"/><rect x="8" y="11" width="8" height="2" fill="#fff"/></symbol>
    <symbol id="icon-leaf" viewBox="0 0 24 24"><path d="M4 20C4 10 10 4 21 3c0 11-6 17-15 17z" fill="#1d2416"/><path d="M4 20L15 9" stroke="#fff" stroke-width="1.5"/></symbol>
    <symbol id="icon-tree" viewBox="0 0 24 24"><circle cx="12" cy="8" r="6" fill="#1d2416"/><circle cx="6.5" cy="11" r="3.5" fill="#1d2416"/><circle cx="17.5" cy="11" r="3.5" fill="#1d2416"/><rect x="11" y="12" width="2" height="9" fill="#1d2416"/></symbol>
  </defs>
</svg>

<section class="flyer flyer--back">
  <div class="photo back-photo" role="img" aria-label="Photo of the health coach seated cross-legged on a lawn"></div>
  <div class="back-heading">
    <h2 class="name">Clara Benson</h2>
    <p class="credentials">BA in Sport and Exercise Management<br>M Pharmacy</p>
  </div>
  <div class="brand back-brand"><span class="brand-dot"></span>Our Vital Ledger</div>

  <h3 class="section-title">Additional <b>Services</b></h3>
  <ul class="service-list service-list--a">
    <li>Holistic health check-up</li>
    <li>Weight-loss goals</li>
    <li>Mini medication reviews</li>
    <li>Review of vitamins and supplements</li>
    <li>Nutritional guidance</li>
    <li>Exercise guidance</li>
  </ul>
  <ul class="service-list service-list--b">
    <li>Use of natural therapies</li>
    <li>Sleep management</li>
    <li>Stress management</li>
    <li>Specific health concerns</li>
    <li>Long term disease and lifestyle management</li>
    <li>Food tips and education</li>
  </ul>

  <div class="contact-band back-band">
    <span class="mini-icon"><svg><use href="#icon-bowl"/></svg></span>
    <span class="mini-icon"><svg><use href="#icon-dumbbell"/></svg></span>
    <span class="mini-icon"><svg><use href="#icon-leaf"/></svg></span>
    <span class="mini-icon"><svg><use href="#icon-tree"/></svg></span>
    <span class="cta">Contact me today</span>
    <p class="phones">0412 608 317<br>(02) 9380 2741</p>
  </div>
</section>

<section class="flyer flyer--front">
  <div class="scene" role="img" aria-label="Sunlit coastal grassland backdrop"></div>
  <div class="front-strip"></div>
  <div class="photo front-photo" role="img" aria-label="Photo of the health coach standing in a white top"></div>
  <div class="brand front-brand"><span class="brand-dot"></span>Our Vital Ledger</div>

  <div class="front-heading">
    <h1 class="name">Clara Benson</h1>
    <p class="tagline">Qualified Holistic<br>Health Coach</p>
  </div>

  <div class="feature-row">
    <div class="feature"><span class="feature-icon"><svg><use href="#icon-bowl"/></svg></span><b>Nutritional</b>Advice</div>
    <div class="feature"><span class="feature-icon"><svg><use href="#icon-dumbbell"/></svg></span><b>Fitness</b>Planning</div>
    <div class="feature"><span class="feature-icon"><svg><use href="#icon-leaf"/></svg></span><b>Natural Health</b>Management</div>
    <div class="feature"><span class="feature-icon"><svg><use href="#icon-tree"/></svg></span><b>Lifestyle</b>Assessment</div>
  </div>

  <div class="contact-band front-band">
    <span class="cta">Contact me today</span>
    <p class="phones">0412 608 317<br>(02) 9380 2741</p>
    <p class="web">www.ourvitalledger.com.au<br>clara@ourvitalledger.com.au</p>
  </div>
</section>

</body>
</html>
```